Postcard Front / Back For Computer Store with IT services

We are a computer store located in Hawaii on the island of Kauai. We would like to have a post card designed to market our services that we offer. We are a PC and Mac repair shop with full retail services.website: www.reefbyteshop.com the first thing that comes up is our service plan, we would like to market that, if you notice we have it Hawaii, meaning the background matches where we live etc, we would like to have the post card themed Hawaii.We offer a bunch of different Service contract Options for our customers:Signle computer 24.99/month Family Plan 29.99/month Business Plan 49.99/per computer month We also offer backup services much like vaultwisp but our own brand starting at 9.99/month.

website address https://www.reefbyteshop.com/online-backup/ for backup offerings..

Target Market(s)

Computer repair, IT services, Online backup, Remote Help Desk

Industry/Entity Type

Computer Repair

Requirements
Must have
• Should have front and Back color
• Phone number 808-519-3371
• website address www.reefbyteshop.com
Nice to have
• Plorin map with location on map
• Store hours mon - friday 9am - 6pm

```html
<!DOCTYPE html>
<html lang="en">
<head>
<meta charset="utf-8">
<title>Reef Byte Shop Postcard</title>
<link href="https://fonts.googleapis.com/css2?family=Open+Sans:wght@400;600;700;800&display=swap" rel="stylesheet">
<style>
  :root {
    --navy: #0d2340;
    --navy-deep: #081a30;
    --blue: #1f7fc4;
    --teal: #1aa3d6;
    --green: #7cc242;
    --green-dark: #5aa12a;
    --ink: #2b3440;
    --grey: #5d6670;
    --paper: #ffffff;
    --bg: #e8e6e2;
    --stamp: #d6d8db;
  }
  * { box-sizing: border-box; margin: 0; padding: 0; }
  html, body { width: 826px; height: 1200px; overflow: hidden; }
  body { background: var(--bg); font-family: "Open Sans", Arial, sans-serif; color: var(--ink); position: relative; }

  .card { position: absolute; left: 33px; width: 760px; height: 506px; background: var(--paper); overflow: hidden; box-shadow: 0 2px 8px rgba(0,0,0,.18); }
  .card--front { top: 60px; }
  .card--back { top: 634px; }

  /* Front */
  .hero-photo { position: absolute; left: 0; top: 0; width: 340px; height: 246px;
    background: linear-gradient(135deg, #dfe8f0 0%, #8fb2cf 45%, #1d4b78 100%); }
  .hero-panel { position: absolute; left: 340px; top: 0; width: 420px; height: 246px; background: var(--navy); }
  .headline { position: absolute; right: 26px; top: 20px; text-align: right; color: #fff; }
  .headline__main { font-size: 40px; font-weight: 800; line-height: 1.05; }
  .headline__sub { font-size: 28px; font-weight: 600; line-height: 1.2; }
  .backup-band { position: absolute; left: 0; right: 0; top: 118px; height: 70px; background: var(--green);
    display: flex; align-items: center; justify-content: flex-end; padding: 0 26px; }
  .backup-band p { color: #fff; font-size: 14px; font-weight: 600; text-align: right; line-height: 1.35; max-width: 290px; }
  .contact { position: absolute; right: 26px; top: 200px; color: #fff; font-size: 24px; font-weight: 800; line-height: 34px; }
  .service-bar { position: absolute; left: 0; top: 246px; width: 760px; height: 44px; background: var(--blue);
    color: #fff; font-size: 15px; font-weight: 700; display: flex; align-items: center; justify-content: flex-end; padding-right: 26px; }

  .brand { position: absolute; left: 28px; top: 312px; display: flex; align-items: center; gap: 10px; }
  .brand__mark { width: 22px; height: 22px; border-radius: 50%; background: var(--green); }
  .brand__name { font-size: 24px; font-weight: 800; color: var(--blue); }

  .plans { position: absolute; left: 28px; top: 360px; width: 280px; list-style: none; }
  .plans li { display: flex; align-items: flex-start; gap: 10px; font-size: 16px; font-weight: 600; color: var(--grey); line-height: 22px; margin-bottom: 4px; }
  .plans svg { flex: none; margin-top: 5px; }

  .since { position: absolute; left: 336px; top: 352px; color: var(--teal); font-size: 32px; font-weight: 700; line-height: 1.1; white-space: nowrap; }
  .since span { display: block; }

  .server-photo { position: absolute; right: 26px; top: 302px; width: 170px; height: 146px;
    background: linear-gradient(160deg, #5a6470 0%, #1b2129 70%); border-radius: 4px; }

  .visit-bar { position: absolute; left: 0; bottom: 0; width: 760px; height: 46px; background: #2e3440;
    color: #fff; font-size: 18px; font-weight: 600; display: flex; align-items: center; padding-left: 28px; }

  /* Back */
  .offer { position: absolute; left: 0; top: 0; width: 330px; height: 506px; background: var(--green); }
  .offer__price { position: absolute; left: 0; top: 0; width: 330px; height: 104px; background: var(--teal);
    color: #fff; text-align: center; padding-top: 12px; }
  .offer__amount { font-size: 40px; font-weight: 800; line-height: 1.05; }
  .offer__setup { font-size: 28px; font-weight: 800; line-height: 1.1; }
  .offer__list { position: absolute; left: 10px; top: 112px; width: 310px; height: 262px; background: #fff;
    list-style: none; padding: 14px 14px; }
  .offer__list li { display: flex; align-items: center; gap: 7px; font-size: 10.5px; color: var(--grey); line-height: 29px; }
  .offer__list li::before { content: ""; width: 6px; height: 6px; border-radius: 50%; background: var(--teal); flex: none; }
  .order-btn { position: absolute; left: 55px; top: 386px; width: 220px; height: 46px; border-radius: 23px;
    background: var(--green-dark); border: 3px solid #fff; color: #fff; font-size: 24px; font-weight: 800;
    display: flex; align-items: center; justify-content: center; }
  .offer__site { position: absolute; left: 0; bottom: 0; width: 330px; height: 60px; background: var(--navy-deep);
    color: #fff; font-size: 17px; font-weight: 600; display: flex; align-items: center; justify-content: center; }
  .stamp { position: absolute; right: 32px; top: 30px; width: 66px; height: 66px; background: var(--stamp); }
</style>
</head>
<body>

  <section class="card card--front">
    <div class="hero-photo" role="img" aria-label="Businessman holding a tablet with glowing network icons"></div>
    <div class="hero-panel">
      <div class="headline">
        <div class="headline__main">If You Notice</div>
        <div class="headline__sub">We have it Hawaii</div>
      </div>
      <div class="backup-band">
        <p>We also offer backup services much like Nimbrel but our own brand starting at 9.99/month.</p>
      </div>
      <div class="contact">Contact us: 808-519-3371</div>
    </div>
    <div class="service-bar">We provide exceptional customer service</div>

    <div class="brand">
      <span class="brand__mark"></span>
      <span class="brand__name">Reef Byte Shop</span>
    </div>

    <ul class="plans">
      <li><svg width="12" height="12" viewBox="0 0 12 12"><circle cx="6" cy="6" r="6" fill="#1aa3d6"/></svg>Signle computer 24.99/month</li>
      <li><svg width="12" height="12" viewBox="0 0 12 12"><circle cx="6" cy="6" r="6" fill="#1aa3d6"/></svg>Family Plan 29.99/month</li>
      <li><svg width="12" height="12" viewBox="0 0 12 12"><circle cx="6" cy="6" r="6" fill="#1aa3d6"/></svg>Business Plan 49.99/per computer month</li>
    </ul>

    <div class="since"><span>Since 2006</span><span>In Hawaii</span></div>

    <div class="server-photo" role="img" aria-label="Row of black server towers"></div>

    <div class="visit-bar">Please Visit Us at: www.reefbyteshop.com</div>
  </section>

  <section class="card card--back">
    <div class="offer">
      <div class="offer__price">
        <div class="offer__amount">$24.99 / MO</div>
        <div class="offer__setup">FREE SETUP</div>
      </div>
      <ul class="offer__list">
        <li>Unlimited virus removal for PCs and Macs ($129 value)</li>
        <li>Unlimited computer tune-ups ($99 value)</li>
        <li>Remote help desk access, any time</li>
        <li>Priority in-store repair service</li>
        <li>Discounts on parts and upgrades</li>
        <li>Data transfer to new devices</li>
        <li>Online backup starting at $9.99</li>
        <li>Unlimited phone support (M–F 9am–6pm)</li>
      </ul>
      <div class="order-btn">ORDER NOW!</div>
      <div class="offer__site">www.reefbyteshop.com</div>
    </div>
    <div class="stamp"></div>
  </section>

</body>
</html>
```